Research Flier

I need to take a very bad flier that I made and turn it into an amazing flyer for my research group to be shared at a high profile conference.

```html
<!DOCTYPE html>
<html lang="en">
<head>
<meta charset="utf-8">
<title>The Kinship Lab – Research Flier</title>
<link rel="stylesheet" href="https://fonts.googleapis.com/css2?family=Archivo+Black&family=Barlow+Condensed:wght@700;800&family=Barlow+Semi+Condensed:ital,wght@0,400;0,500;0,600;1,500&display=swap">
<style>
:root{
  --ink:#000;
  --paper:#fff;
  --green:#88c985;
  --green-head:#76c073;
  --text-dark:#1c1c1c;
  --rule:#b9e0b6;
  --grey:#555;
}
*{box-sizing:border-box;margin:0;padding:0}
html,body{width:800px;height:1200px;overflow:hidden;background:var(--paper)}
body{font-family:"Barlow Semi Condensed",sans-serif;color:var(--text-dark)}
.flier{position:relative;width:800px;height:1200px;background:var(--paper)}
svg{display:block;overflow:visible}
.display-heavy{font-family:"Archivo Black",sans-serif}
.display-cond{font-family:"Barlow Condensed",sans-serif;font-weight:800}

/* left column */
.title-panel{position:absolute;left:0;top:0;width:286px;height:742px;background:var(--ink);color:var(--paper)}
.lab-name{position:absolute;left:21px;top:60px;width:244px;height:245px}
.lab-name text{fill:var(--paper)}
.mission{position:absolute;left:22px;top:387px;width:248px}
.mission-title text{fill:var(--green-head)}
.mission p{font-size:13.5px;line-height:17px;margin-top:13px;font-weight:500}
.mission p:first-of-type{margin-top:12px}

.impact-panel{position:absolute;left:0;top:742px;width:286px;height:340px;background:var(--green);padding:40px 26px 0 26px;color:var(--text-dark)}
.impact-lead{font-style:italic;font-weight:600;font-size:14px;line-height:18px;color:var(--paper)}
.impact-list{list-style:none;margin-top:14px}
.impact-list li{font-size:13px;line-height:16.5px;padding:8px 0 10px;border-bottom:1px solid var(--rule);max-width:190px}
.impact-list li:last-child{border-bottom:none;max-width:210px}

.partner{position:absolute;left:0;top:1082px;width:286px;height:118px;display:flex;align-items:center;gap:12px;padding-left:40px}
.partner-dot{width:38px;height:38px;border-radius:50%;background:#2f74c8;flex:none}
.partner-name{font-size:11.5px;line-height:13px;color:var(--grey)}
.partner-name strong{display:block;font-weight:500;font-size:12.5px;letter-spacing:.5px;margin-top:6px;color:#333}

/* right column */
.masthead{position:absolute;left:286px;top:0;width:514px;height:147px;display:flex;align-items:center;justify-content:center;gap:22px;border-bottom:7px solid var(--green)}
.brand{display:flex;align-items:center;gap:10px}
.brand-dot{width:40px;height:40px;border-radius:50%;background:#e0512a}
.brand-name{font-weight:500;font-size:30px;line-height:30px;color:#2a2a2a;letter-spacing:1px;text-transform:uppercase}
.brand-divider{width:1px;height:56px;background:#999}
.unit{display:flex;flex-direction:column;align-items:center;gap:4px}
.unit-dot{width:26px;height:26px;border-radius:50%;background:#2a2a2a}
.unit-name{font-weight:500;font-size:11px;letter-spacing:.5px;color:#2a2a2a}

.photo{position:absolute;left:286px;top:153px;width:514px;height:285px;background:linear-gradient(180deg,#d9d3c7 0%,#b9a892 35%,#6b5a4f 62%,#a7805f 85%,#c9876a 100%)}

.sites{position:absolute;left:286px;top:438px;width:514px;height:312px;background:var(--green);padding:22px 28px 0 28px}
.sites .section-title text{fill:var(--ink)}
.sites-intro{font-style:italic;font-weight:500;font-size:13.5px;line-height:17px;margin-top:8px}
.site-row{display:grid;gap:6px;margin-top:14px}
.site-row.six{grid-template-columns:repeat(6,1fr)}
.site-row.five{grid-template-columns:1.15fr 1.15fr 1.1fr 1.25fr 1fr;margin-top:12px}
.site h3{font-weight:500;font-size:13px;margin-bottom:3px}
.site ul{list-style:none}
.site li{font-size:7.5px;line-height:9.5px}
.site li::before{content:"• "}

.building{position:absolute;left:286px;top:750px;width:514px;height:410px;padding:30px 10px 0 20px}
.building .section-title{margin-left:8px}
.building .section-title text{fill:var(--green-head)}
.domains{display:grid;grid-template-columns:115px 121px 142px 1fr;margin-top:24px}
.domain{padding-right:8px}
.domain h4{font-family:"Barlow Condensed",sans-serif;font-weight:700;font-size:13.5px;line-height:15px;text-transform:uppercase;letter-spacing:.2px;white-space:nowrap;min-height:15px}
.domain p{font-size:12.5px;line-height:16.5px;margin-top:6px;margin-bottom:18px}
.domain.tall{grid-row:span 2}

.footer{position:absolute;left:286px;top:1160px;width:514px;height:40px;background:var(--green);display:flex;align-items:center;justify-content:center;font-weight:500;font-size:21px;letter-spacing:5px;color:var(--paper)}
</style>
</head>
<body>
<main class="flier">

  <section class="title-panel">
    <h1 class="lab-name" aria-label="The Kinship Lab">
      <svg width="244" height="245" viewBox="0 0 244 245" aria-hidden="true">
        <text class="display-heavy" x="0" y="74" font-size="100" textLength="239" lengthAdjust="spacingAndGlyphs">THE</text>
        <text class="display-cond" x="4" y="149" font-size="86" textLength="228" lengthAdjust="spacingAndGlyphs">KINSHIP</text>
        <text class="display-heavy" x="2" y="241" font-size="100" textLength="229" lengthAdjust="spacingAndGlyphs">LAB</text>
      </svg>
    </h1>
    <div class="mission">
      <h2 class="mission-title" aria-label="Mission">
        <svg width="112" height="34" viewBox="0 0 112 34" aria-hidden="true"><text class="display-cond" x="0" y="33" font-size="46" textLength="110" lengthAdjust="spacingAndGlyphs">MISSION</text></svg>
      </h2>
      <p>Supporting the development of the evidence-based, Open Heart Learning program and CKT for Educators by assessing program implementation and examining feasibility, impact, and long-term sustainability at the school, district, city, and national levels.</p>
      <p>Developing effective tools and measures to CKT and Open Heart Learning</p>
      <p>Support global dissemination through impactful manualization</p>
      <p>Contribute to compassion-based education studies worldwide through scientific advancements that examine compassion, common humanity, wellbeing, interdependence, and secular ethics.</p>
    </div>
  </section>

  <section class="impact-panel">
    <p class="impact-lead">To meaningfully impact change,<br>we have:</p>
    <ul class="impact-list">
      <li>Identified seven critical domains for whole-school implementation sustainment</li>
      <li>Conducted studies on sustainable implementation and its impact on compassionate systems</li>
      <li>Begun work on global implementation frameworks, monitoring guides, and whole-school trainings</li>
    </ul>
  </section>

  <div class="partner">
    <span class="partner-dot"></span>
    <p class="partner-name">Center for<br>Reflective Science and<br>Caring Ethics<strong>LAKEVIEW UNIVERSITY</strong></p>
  </div>

  <header class="masthead">
    <div class="brand"><span class="brand-dot"></span><span class="brand-name">Open Heart<br>Learning</span></div>
    <span class="brand-divider"></span>
    <div class="unit"><span class="unit-dot"></span><span class="unit-name">RESEARCH</span></div>
  </header>

  <div class="photo" role="img" aria-label="Group photo of educators holding training certificates in a school gym with colourful shade sails"></div>

  <section class="sites">
    <h2 class="section-title" aria-label="Research Sites">
      <svg width="245" height="38" viewBox="0 0 245 38" aria-hidden="true"><text class="display-cond" x="0" y="37" font-size="53" textLength="245" lengthAdjust="spacingAndGlyphs">RESEARCH SITES</text></svg>
    </h2>
    <p class="sites-intro">We collaborate with global affiliates to conduct collaborative region-specific research. Read below to discover the impactful projects from our worldwide network!</p>
    <div class="site-row six">
      <div class="site"><h3>USA</h3><ul><li>Several Studies of Late Elementary and Middle</li><li>Multiple School Districts</li><li>Implementation, RCT, Quasi-experimental, Qualitative, and Mixed Methods</li></ul></div>
      <div class="site"><h3>Sweden</h3><ul><li>Late Elementary</li><li>2 Schools</li><li>Feasibility &amp; Qualitative Impact Study</li></ul></div>
      <div class="site"><h3>Spain</h3><ul><li>Late Elementary</li><li>Multiple Schools Across Two Regions</li><li>Implementation Study</li></ul></div>
      <div class="site"><h3>Ukraine</h3><ul><li>Teachers</li><li>Feasibility &amp; Qualitative Impact Study</li></ul></div>
      <div class="site"><h3>Mongolia</h3><ul><li>Late Elementary to High School</li><li>800 + Students</li><li>6 Schools</li><li>Implementation study</li></ul></div>
      <div class="site"><h3>Mexico</h3><ul><li>Pre-service Course Study</li><li>Feasibility and Preliminary Impact</li></ul></div>
    </div>
    <div class="site-row five">
      <div class="site"><h3>Columbia</h3><ul><li>Late Elementary</li><li>300+ students</li><li>Implementation Study</li><li>Feasibility &amp; Qualitative Impact Study</li></ul></div>
      <div class="site"><h3>Brazil</h3><ul><li>Late Elementary</li><li>Ten Schools</li><li>Randomized Controlled Trial</li><li>Teachers &amp; Students</li></ul></div>
      <div class="site"><h3>Kenya</h3><ul><li>Late Elementary</li><li>2 Schools</li><li>Feasibility &amp; Qualitative Impact Study</li></ul></div>
      <div class="site"><h3>India</h3><ul><li>Late Elementary</li><li>More than 1300 Students</li><li>Urban and Rural</li><li>Implementation studies</li><li>Case Studies</li></ul></div>
      <div class="site"><h3>South Korea</h3><ul><li>Elementary</li><li>Implementation Study</li></ul></div>
    </div>
  </section>

  <section class="building">
    <h2 class="section-title" aria-label="Building for Change">
      <svg width="332" height="38" viewBox="0 0 332 38" aria-hidden="true"><text class="display-cond" x="0" y="37" font-size="53" textLength="332" lengthAdjust="spacingAndGlyphs">BUILDING FOR CHANGE</text></svg>
    </h2>
    <div class="domains">
      <div class="domain"><h4>Adult SEL</h4><p>Professional development includes SEL for adults to create supportive schools.</p></div>
      <div class="domain"><h4>Implementation</h4><p>Sustainable practices involves strategies that embed SEL into the educational landscape of the school</p></div>
      <div class="domain"><h4>Community Engagement</h4><p>Engaging families and communities creates a shared vision that enhances sustainability.</p></div>
      <div class="domain tall"><h4>Student Voice</h4><p>Empowering students to actively participate in and contribute to the SEL process strengthens the school community and supports SEL sustainability</p></div>
      <div class="domain"><h4>District Initiative<br>Alignment</h4><p>Those is leadership need skill and OHL understanding for implementation to thrive.</p></div>
      <div class="domain"><h4>Leadership<br>Development</h4><p>Those is leadership need skill and OHL understanding for implementation to thrive.</p></div>
      <div class="domain"><h4>Communities of<br>Practice</h4><p>Ongoing professional development creates opportunities and spaces to strengthen educator development.</p></div>
    </div>
  </section>

  <footer class="footer">research.lakeview.edu</footer>

</main>
</body>
</html>
```